New Flyer Design Project

We need a flyer for our upcoming Rising Builders Forum.

5th Annual Rising Builders Forum
by the Council for Stewardship of Built Ventures (C-SBuV)
Theme: Step Forward
Date: January 24, 2020
Location: Bluestone Lodge Hotel and Conference Center, San Marcos, TX
#StepForward

This is event is put together by C-SBuV's Rising Builders Ring of Merit. I have a logo for the Ring of Merit, but not something that indicates it's the Rising Builders Ring.

More about the Forum (please don't include on the flyer): This Forum provides a venue to openly discuss issues affecting women in our industry and ideas and strategies to address those issues.

Architecture, Construction and Engineering are all struggling with a tremendous shortage of skilled talent. It is more important than ever for organizations to be able to attract, support and retain a talented workforce and to encourage more women to pursue and build vibrant careers in architecture, engineering and construction. Unfortunately, their attrition rate also remains high in these industries. Developing and retaining a skilled workforce includes identifying and addressing the specific needs of women in our industry. Man or Woman; Male or Female Brain, C-SBuV’s Rising Builders Forum will give you and your team the tools you need to excel as an Employer of Choice and a roadmap for individual continued career planning and success .

This unique Forum provides a venue to engage everyone from executives to those just beginning their careers with active, hands-on sessions and vibrant networking with the best and brightest in the A/E/C industry. In our usual C-SBuV Forum style, Keynotes become table participants and table participants become presenters, encouraging participants to assimilate what they are learning. Join local, state and national leaders and subject matter experts as we candidly explore and address the issues affecting women in our industry .

```html
<!DOCTYPE html>
<html lang="en">
<head>
<meta charset="utf-8">
<title>5th Annual Rising Builders Forum</title>
<link rel="stylesheet" href="https://fonts.googleapis.com/css2?family=Bebas+Neue&family=Montserrat:wght@500;600&family=PT+Serif&display=swap">
<style>
  :root {
    --white: #ffffff;
    --green-light: #63c15f;
    --green-mid: #3f9a52;
    --teal-dark: #1e4a4a;
    --navy: #1b2150;
    --yellow: #f1e44a;
    --yellow-deep: #e2d13a;
    --sky: #a9d7ef;
    --sky-deep: #86c3e6;
    --brand-blue: #2f4fa2;
    --brand-green: #7cb342;
  }
  * { margin: 0; padding: 0; box-sizing: border-box; }
  html, body { width: 848px; height: 1200px; overflow: hidden; background: var(--white); }
  .flyer {
    position: relative;
    width: 848px;
    height: 1200px;
    overflow: hidden;
    font-family: "PT Serif", Georgia, serif;
    color: var(--white);
  }
  .hero-photo {
    position: absolute;
    inset: 0;
    background: linear-gradient(180deg, var(--green-light) 0%, var(--green-light) 30%, var(--green-mid) 55%, var(--teal-dark) 78%, var(--navy) 100%);
  }
  .brand-panel {
    position: absolute;
    left: 0; top: 0;
    width: 392px; height: 173px;
    background: var(--white);
  }
  .brand {
    position: absolute;
    display: flex;
    flex-direction: column;
    align-items: center;
    gap: 10px;
    font-family: "Montserrat", Arial, sans-serif;
    font-weight: 600;
  }
  .brand-mark {
    width: 54px; height: 54px;
    border-radius: 50%;
  }
  .brand--council { left: 40px; top: 30px; width: 140px; }
  .brand--council .brand-mark { background: var(--brand-blue); }
  .brand--council .brand-name { color: var(--brand-blue); font-size: 26px; letter-spacing: 0.5px; }
  .brand--ring { left: 196px; top: 38px; width: 180px; }
  .brand--ring .brand-mark { background: var(--brand-green); }
  .brand--ring .brand-name { color: var(--brand-green); font-size: 20px; }
  .feature-circle {
    position: absolute;
    left: 392px; top: -105px;
    width: 502px; height: 502px;
  }
  .headline {
    position: absolute;
    left: 0; top: 432px;
    width: 848px;
    text-align: center;
    font-family: "Bebas Neue", Impact, sans-serif;
    font-weight: 400;
    line-height: 0.9;
  }
  .headline-line { display: block; font-size: 118px; }
  .headline-line--second { margin-top: 8px; }
  .organizer {
    position: absolute;
    left: 0; top: 680px;
    width: 848px;
    text-align: center;
    font-family: "Montserrat", Arial, sans-serif;
    font-weight: 500;
    font-size: 12px;
    letter-spacing: 2.6px;
    text-transform: uppercase;
  }
  .venue {
    position: absolute;
    right: 456px; top: 910px;
    text-align: right;
    font-size: 37px;
    line-height: 49px;
  }
  .divider {
    position: absolute;
    left: 416px; top: 917px;
    width: 16px; height: 188px;
    background: var(--white);
  }
  .event-date {
    position: absolute;
    left: 466px; top: 898px;
    font-size: 76px;
    line-height: 69px;
  }
  .hashtag {
    position: absolute;
    left: 0; top: 1164px;
    width: 848px;
    text-align: center;
    font-family: "Bebas Neue", Impact, sans-serif;
    font-size: 24px;
  }
</style>
</head>
<body>
<main class="flyer">
  <div class="hero-photo" role="img" aria-label="Group photo of four women professionals in dark blazers standing in front of a construction site, tinted green"></div>

  <header class="brand-panel">
    <div class="brand brand--council">
      <span class="brand-mark"></span>
      <span class="brand-name">C-SBuV</span>
    </div>
    <div class="brand brand--ring">
      <span class="brand-mark"></span>
      <span class="brand-name">Rings of Merit</span>
    </div>
  </header>

  <svg class="feature-circle" viewBox="0 0 502 502" aria-hidden="false">
    <defs>
      <linearGradient id="ringGlow" x1="0" y1="0" x2="1" y2="1">
        <stop offset="0" stop-color="var(--yellow)"/>
        <stop offset="1" stop-color="var(--yellow-deep)"/>
      </linearGradient>
      <linearGradient id="skyTone" x1="0" y1="0" x2="0" y2="1">
        <stop offset="0" stop-color="var(--sky-deep)"/>
        <stop offset="1" stop-color="var(--sky)"/>
      </linearGradient>
    </defs>
    <circle cx="251" cy="251" r="251" fill="url(#ringGlow)"/>
    <circle cx="262" cy="240" r="230" fill="url(#skyTone)" role="img" aria-label="Photo of a red tower crane against a blue sky"/>
  </svg>

  <h1 class="headline">
    <span class="headline-line">5th Annual Rising</span>
    <span class="headline-line headline-line--second">Builders Forum</span>
  </h1>

  <p class="organizer">By the Council for Stewardship of Built Ventures (C-SBuV)</p>

  <p class="venue">Bluestone<br>Lodge Hotel and<br>Conference Center,<br>San Marcos, TX</p>
  <div class="divider"></div>
  <p class="event-date">January<br>24<br>2020</p>

  <p class="hashtag">#StepForward</p>
</main>
</body>
</html>
```